Etiketten-Design für Imkerei
Super Zusammenarbeit. Änderungswünsche wurden sofort berücksichtigt und bearbeitet. Sind mit dem Design richtig happy und können Friederike nur weiterempfehlen.
Zielgruppe
Wir sind eine kleine aber feine Imkerei, die gerade erst begonnen hat. Deshalb sind wir auf der Suche nach einem ansprechenden Design um einen guten Eindruck zu hinterlassen.
Aufgabenstellung
Das Design für unsere Imkerei Wabenglanz sollte möglichst schlicht in den Farben sein . Da wir die Imkerei zu zweit führen, wäre es cool wenn man Elemente einbauen könnte, die darauf hinweisen. (zb.: 2 Blumen, 2 Bienen, 2 Honigtöpfe, 2 Bäume....je nach dem). Wir hätten uns vorgestellt, dass eine verspielte Biene herumschwirrt. Wir werden eine Skizze anfügen, lassen uns aber von eigenen Ideen gerne überzeugen. Außerdem bitte ich auf die Kennzeichnungsverordnung, die in Österreich gilt, acht zu geben. Schriftgröße bei Mengenangabe ist sehr wichtig (wird angefügt).
Wir benötigen die Etiketten in 2 verschiedenen Größen (250g und 500g gleiches Etikett mit 40x140mm(Höhe x Breite), 1000g mit 60x190mm(Höhe x Breite)) jeweils für Blütenhonig und Cremehonig
Wir freuen uns auf viele spannende Entwürfe, sind für alles offen und bedanken uns im Voraus.

```html
<!DOCTYPE html>
<html lang="de">
<head>
<meta charset="utf-8">
<title>Etikett Imkerei Wabenglanz – Blütenhonig</title>
<link rel="stylesheet" href="https://fonts.googleapis.com/css2?family=Montserrat:wght@500;600;700&display=swap">
<style>
  :root {
    --backdrop: #c6c6c6;
    --label: #ffffff;
    --ink: #111111;
    --honey: #f5ad3a;
    --illustration: #f1f1f1;
    --illustration-edge: #e0e0e0;
  }
  html, body {
    margin: 0;
    padding: 0;
    width: 1200px;
    height: 1073px;
    overflow: hidden;
    background: var(--backdrop);
  }
  .canvas {
    position: relative;
    width: 1200px;
    height: 1073px;
    font-family: "Montserrat", Arial, sans-serif;
    color: var(--ink);
  }
  .label {
    position: absolute;
    left: 61px;
    top: 297px;
    width: 1055px;
    height: 420px;
    background: var(--label);
  }
  .illustration {
    position: absolute;
    top: 43px;
    width: 200px;
    height: 304px;
    background: radial-gradient(circle at 50% 50%, var(--illustration) 0%, var(--illustration-edge) 100%);
    border-radius: 36px;
  }
  .illustration--left { left: 10px; }
  .illustration--right { left: 845px; }
  .info {
    position: absolute;
    top: 46px;
    margin: 0;
    font-weight: 600;
    font-size: 20px;
    line-height: 26px;
  }
  .info--ingredients { left: 225px; }
  .info--producer { right: 228px; text-align: right; }
  .seal {
    position: absolute;
    left: 0;
    top: 0;
    width: 1055px;
    height: 420px;
    overflow: visible;
  }
  .seal__ring-text {
    font-family: "Montserrat", Arial, sans-serif;
    font-weight: 600;
    font-size: 24px;
    fill: var(--ink);
  }
  .seal__variety {
    font-family: "Montserrat", Arial, sans-serif;
    font-weight: 700;
    font-size: 30px;
    fill: var(--honey);
  }
  .seal__dashes {
    fill: none;
    stroke: var(--ink);
    stroke-width: 2.5;
    stroke-dasharray: 7 8;
  }
  .seal__rule { stroke: var(--ink); stroke-width: 1.5; }
  .brand {
    position: absolute;
    left: 433px;
    top: 122px;
    width: 200px;
    text-align: center;
    font-weight: 500;
    font-size: 25px;
    line-height: 36px;
    margin: 0;
  }
  .brand__kind { color: var(--honey); }
  .net-weight {
    position: absolute;
    left: 433px;
    top: 234px;
    width: 200px;
    text-align: center;
    font-weight: 700;
    font-size: 40px;
    line-height: 46px;
    margin: 0;
  }
  .storage-note {
    position: absolute;
    left: 0;
    right: 0;
    top: 372px;
    text-align: center;
    font-weight: 600;
    font-size: 21.5px;
    line-height: 30px;
    margin: 0;
  }
</style>
</head>
<body>
<div class="canvas">
  <section class="label">
    <div class="illustration illustration--left" role="img" aria-label="Linienzeichnung: Herz mit zwei Bienen, gestrichelter Flugbahn und Blättern"></div>
    <div class="illustration illustration--right" role="img" aria-label="Linienzeichnung: gespiegeltes Herz mit zwei Bienen, gestrichelter Flugbahn und Blättern"></div>

    <p class="info info--ingredients">Zutaten:<br>Honig,10 %<br>Nuss-mischung<br>(Haselnüsse,<br>Walnüsse)</p>
    <p class="info info--producer">Imkerei<br>Wabenglanz<br>Strasse12345<br>Wohnort<br>Tel.12345678</p>

    <svg class="seal" viewBox="0 0 1055 420">
      <defs>
        <path id="seal-top-arc" d="M 406.5 202 A 127 127 0 1 1 659.5 202"/>
        <path id="seal-bottom-arc" d="M 441.7 299.8 A 142 142 0 0 0 624.3 299.8"/>
      </defs>
      <text class="seal__ring-text"><textPath href="#seal-top-arc" startOffset="50%" text-anchor="middle" textLength="405" lengthAdjust="spacing">österreihischer Bienenhonig</textPath></text>
      <text class="seal__variety"><textPath href="#seal-bottom-arc" startOffset="50%" text-anchor="middle">Blütenhonig</textPath></text>
      <path class="seal__dashes" d="M 405.8 218 A 130 130 0 0 0 436.4 278"/>
      <path class="seal__dashes" d="M 660.2 218 A 130 130 0 0 1 629.6 278"/>
      <line class="seal__rule" x1="418" y1="228" x2="640" y2="228"/>
    </svg>

    <p class="brand"><span class="brand__kind">Imkerei</span><br>Wabenglanz</p>
    <p class="net-weight">250G</p>

    <p class="storage-note">L123456&nbsp; Trocken, dunkel und kühl lagern! Mindestens haltbar bis Ende: 12.2025</p>
  </section>
</div>
</body>
</html>
```